Tri-fold Brochure Design for Law Firm

I need a tri-fold brochure to give to prospective clients.
I have attached a Photoshop design file of a tri-fold brochure. The content (copy) is good, however, he brochure itself looks very amateurish.
I want a professional, sophisticated looking brochure.
The law firm specializes in commercial debt collection.
The law firm is located in New York City.
Our target market is business owners, doctors, lawyers, collection agencies and accountants.
Visit my website which is being designed at www.dorvenlaw.com. I like the font used for the name of my company and the rich blue color used.

Target Market(s)

Business Owners, Doctors, Law Firms and Accountants

Industry/Entity Type

Law Firm

Font styles to use
Serif

Requirements
Must have
• Professional quality graphic work. Attention to details.
• PHOTOGRAPHS ONLY, NO CLIP-ART.
• DARK COLORS - NAVY BLUE, HUNTER GREEN, BLACK, GRAY & WHITE
Nice to have
• I want it to look smart, modern and sophisticated.
• Visit my website which is being designed at www.dorvenlaw.com. I like the font used for the name of my company and the rich blue color used.
Should not have
• Bad artwork
• CLIP ART

```html
<!DOCTYPE html>
<html lang="en">
<head>
<meta charset="utf-8">
<title>Dorven &amp; Company, PLLC – Tri-fold Brochure</title>
<link rel="stylesheet" href="https://fonts.googleapis.com/css2?family=Arimo:wght@400;700&family=Cinzel:wght@600&family=Lato:wght@400;700;900&family=Libre+Baskerville:wght@700&display=swap">
<style>
  :root {
    --navy: #1d3568;
    --navy-deep: #142651;
    --blue-line: #4b6fb0;
    --charcoal: #4a4a4c;
    --ink: #333336;
    --grey-light: #e9eaee;
    --paper: #ffffff;
    --stage: #f1f2f4;
  }
  * { box-sizing: border-box; margin: 0; padding: 0; }
  html, body { width: 1200px; height: 990px; overflow: hidden; background: var(--stage); }
  .brochure {
    position: absolute; left: 30px; top: 55px; width: 1140px; height: 880px;
    display: flex; box-shadow: 0 6px 24px rgba(0,0,0,.18);
  }
  .panel { position: relative; width: 380px; height: 880px; overflow: hidden; background: var(--paper); }
  .panel + .panel { border-left: 1px solid #d8dae0; }
  .panel svg.shapes { position: absolute; inset: 0; width: 380px; height: 880px; }
  .panel-services { background: linear-gradient(180deg, #f4f5f8 0%, var(--grey-light) 60%, #f4f5f8 100%); }

  .tab {
    position: absolute; left: 0; height: 40px; padding: 0 28px 0 26px;
    background: var(--navy); color: var(--paper);
    font: 700 19px/40px "Libre Baskerville", Georgia, serif; letter-spacing: .5px;
    border-radius: 0 22px 22px 0;
  }
  .tab-trusted { top: 68px; }
  .tab-why { top: 578px; }

  .services-content {
    position: absolute; top: 126px; left: 26px; right: 22px;
    font: 400 12px/1.42 "Lato", Arial, sans-serif; color: var(--ink);
  }
  .services-content .intro p + p { margin-top: 6px; }
  .serve-title { margin-top: 14px; font-weight: 700; }
  .serve-columns { display: flex; gap: 8px; margin-top: 6px; }
  .serve-list { list-style: none; line-height: 1.5; }
  .serve-list.col-a { width: 146px; }
  .serve-list.col-b { flex: 1; }
  .serve-list li { padding-left: 9px; text-indent: -9px; }
  .serve-list li::before { content: "• "; color: var(--navy); }

  .why {
    position: absolute; top: 630px; left: 26px; right: 22px;
    font: 400 12px/1.42 "Lato", Arial, sans-serif; color: var(--ink);
  }
  .why strong { display: block; font-weight: 700; margin-bottom: 3px; }

  .footer-url {
    position: absolute; left: 0; right: 0; bottom: 18px; text-align: center;
    font: 700 15px "Lato", Arial, sans-serif; letter-spacing: 4px; color: var(--paper);
  }

  .contact-block { position: absolute; top: 112px; left: 20px; right: 20px; text-align: center; color: var(--ink); font: 400 13px/1.45 "Lato", Arial, sans-serif; }
  .firm-name, .attorney-name { font: 700 16px/1.3 "Libre Baskerville", Georgia, serif; color: var(--navy); }
  .attorney-name { margin-top: 12px; }
  .tagline { margin-top: 4px; }
  .office-heading {
    display: inline-block; margin-top: 22px; padding-bottom: 2px;
    font: 700 15px "Libre Baskerville", Georgia, serif; color: var(--navy);
    border-bottom: 2px solid var(--navy); text-transform: uppercase;
  }
  .address { margin-top: 6px; text-transform: uppercase; }

  .quick-contact { position: absolute; left: 40px; top: 660px; list-style: none; color: var(--paper); font: 700 17px/1.6 "Arimo", Arial, sans-serif; }

  .cover-name { position: absolute; top: 48px; left: 0; right: 0; text-align: center; color: var(--paper); font: 600 24px/1.1 "Cinzel", Georgia, serif; }
  .cover-name small { display: block; margin-top: 6px; font-size: 15px; letter-spacing: 1px; }
  .cover-photo {
    position: absolute; left: 0; top: 170px; width: 380px; height: 480px;
    background: linear-gradient(180deg, #5b8fd1 0%, #9cc0ea 35%, #dfe4e8 62%, #b9b3a6 85%, #8f8a80 100%);
  }
  .cover-title { position: absolute; right: 30px; top: 676px; text-align: right; }
  .cover-kicker { font: 400 23px "Arimo", Arial, sans-serif; color: var(--navy); letter-spacing: .5px; }
  .cover-headline { font: 700 64px/1 "Arimo", Arial, sans-serif; color: var(--charcoal); letter-spacing: 1px; }
</style>
</head>
<body>
<main class="brochure">

  <section class="panel panel-services">
    <svg class="shapes" viewBox="0 0 380 880" aria-hidden="true">
      <path d="M0,0 H380 V22 Q200,58 0,34 Z" fill="var(--navy)"/>
      <path d="M0,34 Q200,58 380,22 V28 Q200,66 0,40 Z" fill="var(--blue-line)"/>
      <path d="M0,560 Q200,520 380,548 V880 H0 Z" fill="var(--paper)"/>
      <path d="M0,556 Q200,514 380,542 V550 Q200,524 0,564 Z" fill="var(--navy)"/>
      <path d="M0,822 Q200,800 380,812 V880 H0 Z" fill="var(--navy)"/>
      <path d="M0,816 Q200,792 380,805 V812 Q200,800 0,822 Z" fill="var(--blue-line)"/>
    </svg>
    <h2 class="tab tab-trusted">A TRUSTED PARTNER</h2>
    <div class="services-content">
      <div class="intro">
        <p>We under the business of debt collection. Our primary focus is to help our clients secure the payments they are owed. We work closely with both private clients and leading service professionals such as attorneys and accountants, to provide added value to their clients through customized debt collection services.</p>
        <p>We value our relationships as trusted advisors.</p>
      </div>
      <p class="serve-title">We proudly serve:</p>
      <div class="serve-columns">
        <ul class="serve-list col-a">
          <li>Law firms</li>
          <li>Manufacturers</li>
          <li>Collection Agencies</li>
          <li>Factors</li>
          <li>Carting Companies</li>
          <li>Oil Companies</li>
          <li>Publishing and Advertising Companies</li>
        </ul>
        <ul class="serve-list col-b">
          <li>Accounting Firms</li>
          <li>Wholesalers and Distributors</li>
          <li>Financial Service Companies</li>
          <li>Doctors and Healthcare Professionals</li>
          <li>Freight Forwarders &amp; Custom Brokers</li>
          <li>Construction and Real Estate Firms</li>
        </ul>
      </div>
    </div>
    <h2 class="tab tab-why">WHY USE US?</h2>
    <div class="why">
      <strong>Anyone can sue a Debtor</strong>
      It's not difficult to get nasty or to treat people who owe you money in a rude and unprofessional way. However, very few people have the skill, temperament and experience needed to effectively negotiate with Debtors, stakeholders, lawyers, as well as court personnel, sheriffs and marshals to efficiently collect the most money possible in the least amount of time. We truly understand the nature of commercial debt. Collecting money is a specialized skill.
    </div>
    <p class="footer-url">www.dorvenlaw.com</p>
  </section>

  <section class="panel panel-contact">
    <svg class="shapes" viewBox="0 0 380 880" aria-hidden="true">
      <path d="M0,0 H380 V40 Q190,90 0,62 Z" fill="var(--navy)"/>
      <path d="M0,62 Q190,90 380,40 V47 Q190,98 0,69 Z" fill="var(--blue-line)"/>
      <path d="M0,600 Q190,520 380,562 V880 H0 Z" fill="var(--charcoal)"/>
      <path d="M0,588 Q190,500 380,545 V562 Q190,520 0,600 Z" fill="var(--navy)"/>
      <path d="M0,822 Q200,800 380,812 V880 H0 Z" fill="var(--navy)"/>
      <path d="M0,816 Q200,792 380,805 V812 Q200,800 0,822 Z" fill="var(--blue-line)"/>
    </svg>
    <div class="contact-block">
      <p class="firm-name">DORVEN &amp; COMPANY, PLLC</p>
      <p class="tagline">Debt Collection Attorneys In New York State</p>
      <p class="attorney-name">MARCUS J. DORVEN, ESQUIRE</p>
      <p>President<br>mdorven@dorvenlaw.com<br>(212) 555-0193 Cell</p>
      <h3 class="office-heading">Westchester County Office</h3>
      <p class="address">412 Ridgefield Avenue, Suite 204<br>White Plains, New York 10601<br>(Off Exit 6 on EB Interstate 287)</p>
      <h3 class="office-heading">Mailing Address</h3>
      <p class="address">96 Lexington Row, Suite 3120<br>New York, New York 10016-0000</p>
    </div>
    <ul class="quick-contact">
      <li>TOLL FREE: (877) 555-0142</li>
      <li>LOCAL: (212) 555-0108</li>
      <li>FAX: (917) 555-0118</li>
      <li>www.DorvenLaw.com</li>
    </ul>
    <p class="footer-url">www.dorvenlaw.com</p>
  </section>

  <section class="panel panel-cover">
    <div class="cover-photo" role="img" aria-label="Photograph of a domed capitol building with columns under a blue sky with clouds"></div>
    <svg class="shapes" viewBox="0 0 380 880" aria-hidden="true">
      <path d="M0,0 H380 V150 Q190,215 0,190 Z" fill="var(--navy)"/>
      <path d="M0,190 Q190,215 380,150 V178 Q190,240 0,212 Z" fill="var(--charcoal)"/>
      <path d="M0,212 Q190,240 380,178 V184 Q190,247 0,218 Z" fill="var(--paper)"/>
      <path d="M0,660 Q200,610 380,628 V880 H0 Z" fill="var(--paper)"/>
      <path d="M0,650 Q200,598 380,616 V630 Q200,612 0,662 Z" fill="var(--navy)"/>
      <path d="M0,822 Q200,800 380,812 V880 H0 Z" fill="var(--navy)"/>
      <path d="M0,816 Q200,792 380,805 V812 Q200,800 0,822 Z" fill="var(--blue-line)"/>
    </svg>
    <h1 class="cover-name">Dorven &amp; Company, PLLC<small>Attorneys At Law</small></h1>
    <div class="cover-title">
      <p class="cover-kicker">A NEW YORK BASED</p>
      <p class="cover-headline">LAW FIRM</p>
    </div>
    <p class="footer-url">www.DorvenLaw.com</p>
  </section>

</main>
</body>
</html>
```